Fitness & sports performance company needs a landing page design

Looking for a landing page for a fitness & sports performance company based in South Florida. The company is 'The Lantern Athletic Club', and 'The Lantern' for short. The main objective of the landing page is to generate leads, and show potential clients the services we offer, as well as pricing for each service. While we are based in South Florida, we also offer online services such as an online trainer and online strength & conditioning programs. Would like to see designs that utilize the colors in our logo.

Target Market(s)

those looking to lose weight, gain strength and make overall healthy lifestyle changes

Font styles to use
Sans Serif

Colors
60b9df
57b5de

Requirements
Must have
• a place to list testimonials, list of services provided, show pricing for each service, colors of the website matching colors in the logo
Nice to have
• i would like to see a landing page that can be utilized to create leads and an email list

```html
<!DOCTYPE html>
<html lang="en">
<head>
<meta charset="utf-8">
<title>The Lantern Athletic Club – Fitness &amp; Sports</title>
<link href="https://fonts.googleapis.com/css2?family=Josefin+Sans:wght@400;600;700&family=Mulish:wght@400;600;700&display=swap" rel="stylesheet">
<style>
:root{
  --accent:#3ec3d0;
  --accent-dark:#2fa9b6;
  --ink:#111;
  --white:#fff;
  --muted:#777;
  --field:#f3f3f3;
  --night:#000;
  --hero-a:#5b5f63;
  --hero-b:#1f2226;
}
*{box-sizing:border-box;margin:0;padding:0}
html,body{width:1200px;height:3805px;overflow:hidden}
body{position:relative;background:var(--white);font-family:"Mulish",Arial,sans-serif;color:var(--ink)}
section,header,footer,nav{position:absolute;left:0;width:1200px}
.btn{position:absolute;display:flex;align-items:center;justify-content:center;gap:12px;background:var(--accent);color:var(--white);font:700 13px "Josefin Sans",sans-serif;letter-spacing:.5px;text-transform:uppercase}
.btn svg{width:10px;height:14px}

/* nav */
.topnav{top:0;height:46px;background:var(--night);display:flex;justify-content:center;align-items:stretch}
.topnav a{color:var(--white);text-decoration:none;font:400 14px "Mulish",sans-serif;padding:0 14px;display:flex;align-items:center}
.topnav a.active{background:var(--accent)}

.brandbar{top:46px;height:111px;display:flex;align-items:center;justify-content:center;gap:14px}
.brandbar .dot{width:54px;height:54px;border-radius:50%;background:var(--accent)}
.brandbar .name{font:700 22px "Josefin Sans",sans-serif;color:var(--ink);letter-spacing:1px}

/* hero */
.hero{top:157px;height:635px;background:radial-gradient(ellipse at 50% 35%,#8a8d90 0%,var(--hero-a) 35%,var(--hero-b) 100%)}
.hero .photo{position:absolute;inset:0}
.hero h1{position:absolute;top:218px;left:0;width:100%;text-align:center;color:var(--white);font:600 84px/96px "Josefin Sans",sans-serif;letter-spacing:1px}
.hero p{position:absolute;top:330px;left:250px;width:700px;text-align:center;color:var(--white);font-size:14px;line-height:20px}
.hero .hero-cta{left:508px;top:398px;width:195px;height:42px}
.hero .dots{position:absolute;top:594px;left:578px;display:flex;gap:8px}
.hero .dots span{width:10px;height:10px;border-radius:50%;background:rgba(255,255,255,.6)}
.hero .dots span.on{background:var(--accent)}

/* about */
.about{top:792px;height:461px}
.about .intro{position:absolute;left:0;top:0;width:533px;height:461px;background:var(--white)}
.about h2{position:absolute;left:122px;top:148px;font:700 27px "Josefin Sans",sans-serif}
.about .intro p{position:absolute;left:122px;top:205px;width:340px;font-size:13px;line-height:18px;color:var(--muted)}
.about .video{position:absolute;left:533px;top:0;width:667px;height:461px;background:linear-gradient(120deg,#3a3d40,#141618 70%)}
.about .video .kicker{position:absolute;left:71px;top:227px;color:var(--white);font-size:15px}
.about .video h3{position:absolute;left:71px;top:252px;color:var(--white);font:600 29px "Josefin Sans",sans-serif}
.about .video p{position:absolute;left:71px;top:290px;width:360px;color:var(--white);font-size:14px;line-height:19px}
.about .watch{position:absolute;left:71px;top:358px;display:flex;align-items:center;gap:16px;color:var(--white);font:600 14px "Josefin Sans",sans-serif}
.about .watch svg{width:40px;height:40px}

/* services */
.services{top:1253px;height:541px;background:linear-gradient(100deg,#2a2c2e,#4d4f51 45%,#2b2d2f)}
.section-title{position:absolute;left:0;width:100%;text-align:center;font:700 26px "Josefin Sans",sans-serif}
.services .section-title{top:66px;color:var(--white)}
.service{position:absolute;top:136px;width:180px;text-align:center;color:var(--white)}
.service .icon{width:178px;height:178px;border-radius:50%;background:var(--accent);margin:0 auto;display:flex;align-items:center;justify-content:center}
.service .icon svg{width:64px;height:64px}
.service h4{margin-top:38px;font:700 16px "Josefin Sans",sans-serif}
.service .price{font:600 17px "Josefin Sans",sans-serif;margin-top:2px}
.service .per{font-size:12px;margin-top:-2px}

/* courses */
.courses{top:1794px;height:578px;background:var(--white)}
.courses .section-title{top:58px;color:var(--ink)}
.courses .arrows{position:absolute;top:62px;left:1006px;display:flex;gap:8px}
.courses .arrows span{width:34px;height:34px;border-radius:50%;display:flex;align-items:center;justify-content:center}
.courses .arrows .prev{border:1px solid #999}
.courses .arrows .next{background:var(--accent)}
.course{position:absolute;top:132px;height:294px}

/* trainers */
.trainers{top:2372px;height:538px;background:linear-gradient(90deg,#141516,#2e3032 50%,#111213)}
.trainers .section-title{top:60px;color:var(--white)}
.trainer{position:absolute;top:119px;width:254px;height:270px}
.trainer .arch{position:absolute;inset:0}
.trainer .portrait{position:absolute;left:42px;top:64px;width:152px;height:152px;border-radius:50%;background:linear-gradient(160deg,#8b7d6f,#3f3a36)}
.trainer h4{position:absolute;left:86px;top:220px;color:var(--white);font:700 26px "Josefin Sans",sans-serif;white-space:nowrap}
.trainer .social{position:absolute;left:86px;top:250px;display:flex;gap:5px}
.trainer .social span{width:13px;height:13px;border-radius:50%;background:var(--accent)}

/* contact */
.contact{top:2910px;height:464px;background:var(--white)}
.contact .map{position:absolute;left:0;top:0;width:601px;height:464px;background:linear-gradient(150deg,#e6e4df,#d9dcd6 55%,#c7d9e6)}
.contact .section-title{left:601px;width:599px;top:66px;color:var(--ink)}
.field{position:absolute;left:644px;width:429px;height:43px;background:var(--field);color:#aaa;font-size:12px;padding:14px 14px}
.contact .btn{left:644px;top:368px;width:429px;height:43px}

/* footer */
.site-footer{top:3374px;height:431px;background:var(--night);color:var(--white)}
.site-footer .brand{position:absolute;left:122px;top:46px;display:flex;align-items:center;gap:14px}
.site-footer .brand .dot{width:100px;height:100px;border-radius:50%;background:var(--accent)}
.site-footer .brand .name{font:700 20px "Josefin Sans",sans-serif;color:var(--white)}
.site-footer .blurb{position:absolute;left:122px;top:180px;width:270px;font-size:13px;line-height:17px}
.site-footer .more{position:absolute;left:122px;top:242px;color:var(--accent);font:700 13px "Josefin Sans",sans-serif;border-bottom:1px solid var(--accent)}
.site-footer .social{position:absolute;left:122px;top:284px;display:flex;gap:10px}
.site-footer .social span{width:26px;height:26px;border-radius:50%;background:var(--accent)}
.site-footer h5{position:absolute;top:104px;font:700 15px "Josefin Sans",sans-serif;letter-spacing:.5px}
.site-footer ul{position:absolute;list-style:none;font-size:13px;line-height:16px}
.quick li::before{content:"";display:inline-block;width:5px;height:5px;border-radius:50%;background:var(--accent);margin-right:12px;vertical-align:middle}
.reach li{display:flex;gap:10px;align-items:flex-start;margin-bottom:5px}
.reach svg{width:12px;height:12px;flex:none;margin-top:2px}
.site-footer .news{position:absolute;left:875px;top:180px;width:210px;font-size:13px;line-height:17px}
.site-footer .email{position:absolute;left:875px;top:239px;width:206px;height:30px;border:1px solid var(--white);border-radius:3px;font-size:12px;padding:7px 8px;color:#ccc}
.site-footer .subscribe{left:875px;top:277px;width:206px;height:31px;font-size:12px}
.site-footer .rule{position:absolute;left:122px;top:335px;width:959px;height:1px;background:#555}
.site-footer .legal{position:absolute;top:358px;font-size:12px}
</style>
</head>
<body>

<nav class="topnav">
  <a class="active">Home</a><a>About</a><a>Services</a><a>Classes</a><a>Schedule</a><a>Trainers</a><a>Blog</a><a>Contact</a>
</nav>

<header class="brandbar">
  <span class="dot"></span><span class="name">THE LANTERN</span>
</header>

<section class="hero">
  <div class="photo" role="img" aria-label="Sprinter crouched in starting position on an open road under a stormy sky"></div>
  <h1>FITNESS &amp; SPORTS</h1>
  <p>Lorem Ipsum is simply dummy text of the printing and typesetting industry. Lorem Ipsum has been the industry's standard dummy text ever since the 1500s.</p>
  <div class="btn hero-cta">Learn More <svg viewBox="0 0 10 14"><path d="M2 1l6 6-6 6" fill="none" stroke="#fff" stroke-width="2"/></svg></div>
  <div class="dots"><span></span><span class="on"></span><span></span></div>
</section>

<section class="about">
  <div class="intro">
    <h2>ABOUT US</h2>
    <p>Lorem Ipsum is simply dummy text of the printing and typesetting industry. Lorem Ipsum has been the industry's standard dummy text ever since the 1500s.</p>
    <div class="btn" style="left:122px;top:299px;width:193px;height:43px">Learn More <svg viewBox="0 0 10 14"><path d="M2 1l6 6-6 6" fill="none" stroke="#fff" stroke-width="2"/></svg></div>
  </div>
  <div class="video" role="img" aria-label="Woman and man training with push-ups in a dark studio">
    <div class="kicker">Are you ready to be amazed?</div>
    <h3>VIDEO INTRODUCTION</h3>
    <p>Lorem Ipsum is simply dummy text of the printing and typesetting industry.</p>
    <div class="watch"><svg viewBox="0 0 40 40"><circle cx="20" cy="20" r="18" fill="none" stroke="#fff" stroke-width="2"/><path d="M16 12l11 8-11 8z" fill="#fff"/></svg>WATCH VIDEO</div>
  </div>
</section>

<section class="services" role="img" aria-label="Athlete in a sprint start inside a warehouse gym">
  <h2 class="section-title">OUR SERVICES</h2>
  <div class="service" style="left:118px">
    <div class="icon"><svg viewBox="0 0 64 64" fill="#fff"><circle cx="38" cy="12" r="6"/><path d="M10 26l22-4 8 2 14-8 3 4-15 11-4 12 8 14-5 3-10-14-10 12-4-3 9-15 2-10-16 2z"/></svg></div>
    <h4>AEROBICS</h4><div class="price">$150</div><div class="per">PER MONTH</div>
  </div>
  <div class="service" style="left:316px">
    <div class="icon"><svg viewBox="0 0 64 64" fill="#fff"><circle cx="36" cy="14" r="6"/><path d="M24 26h16l6 10H20z"/><rect x="8" y="40" width="48" height="6"/><rect x="10" y="46" width="4" height="10"/><rect x="50" y="46" width="4" height="10"/></svg></div>
    <h4>SPA &amp; WELLNESS</h4><div class="price">$150</div><div class="per">PER MONTH</div>
  </div>
  <div class="service" style="left:511px">
    <div class="icon"><svg viewBox="0 0 64 64" fill="#fff"><circle cx="32" cy="26" r="8"/><path d="M14 50c0-10 8-16 18-16s18 6 18 16z"/><path d="M24 8c3 3-3 5 0 8M32 6c3 3-3 5 0 8M40 8c3 3-3 5 0 8" fill="none" stroke="#fff" stroke-width="2"/><ellipse cx="32" cy="52" rx="24" ry="5" fill="none" stroke="#fff" stroke-width="2"/></svg></div>
    <h4>SAUNA</h4><div class="price">$150</div><div class="per">PER MONTH</div>
  </div>
  <div class="service" style="left:704px">
    <div class="icon"><svg viewBox="0 0 64 64" fill="#fff"><rect x="6" y="26" width="6" height="12" rx="1"/><rect x="12" y="20" width="8" height="24" rx="2"/><rect x="20" y="29" width="24" height="6"/><rect x="44" y="20" width="8" height="24" rx="2"/><rect x="52" y="26" width="6" height="12" rx="1"/></svg></div>
    <h4>GYM</h4><div class="price">$150</div><div class="per">PER MONTH</div>
  </div>
  <div class="service" style="left:899px">
    <div class="icon"><svg viewBox="0 0 64 64" fill="#fff"><circle cx="46" cy="20" r="5"/><path d="M10 30l14-10 10 8-8 4z"/><path d="M6 42c5-4 9-4 13 0s9 4 13 0 9-4 13 0 9 4 13 0M6 50c5-4 9-4 13 0s9 4 13 0 9-4 13 0 9 4 13 0" fill="none" stroke="#fff" stroke-width="3"/></svg></div>
    <h4>AQUA GYM</h4><div class="price">$150</div><div class="per">PER MONTH</div>
  </div>
  <div class="btn" style="left:510px;top:442px;width:193px;height:43px">View More <svg viewBox="0 0 10 14"><path d="M2 1l6 6-6 6" fill="none" stroke="#fff" stroke-width="2"/></svg></div>
</section>

<section class="courses">
  <h2 class="section-title">OPENING COURSES</h2>
  <div class="arrows">
    <span class="prev"><svg width="10" height="14" viewBox="0 0 10 14"><path d="M8 1L2 7l6 6" fill="none" stroke="#777" stroke-width="2"/></svg></span>
    <span class="next"><svg width="10" height="14" viewBox="0 0 10 14"><path d="M2 1l6 6-6 6" fill="none" stroke="#fff" stroke-width="2"/></svg></span>
  </div>
  <div class="course" style="left:119px;width:317px;background:linear-gradient(160deg,#b9a995,#5d4e41)" role="img" aria-label="Group aerobics class in a bright studio"></div>
  <div class="course" style="left:441px;width:318px;background:linear-gradient(180deg,#9c9a96,#4a4845)" role="img" aria-label="Woman training with battle ropes against a brick wall"></div>
  <div class="course" style="left:764px;width:314px;background:linear-gradient(180deg,#9fc4df,#c9b79c 70%)" role="img" aria-label="Runners jogging along a seaside promenade"></div>
  <div class="btn" style="left:510px;top:484px;width:196px;height:43px">View All Classes <svg viewBox="0 0 10 14"><path d="M2 1l6 6-6 6" fill="none" stroke="#fff" stroke-width="2"/></svg></div>
</section>

<section class="trainers" role="img" aria-label="Athletes training in a dark gym">
  <h2 class="section-title">MEET OUR TRAINERS</h2>
  <div class="trainer" style="left:122px">
    <svg class="arch" viewBox="0 0 254 270"><path d="M14 230V127a113 113 0 0 1 226 0v45" fill="none" stroke="#fff" stroke-width="24"/></svg>
    <div class="portrait" role="img" aria-label="Portrait of trainer Marco Delane"></div>
    <h4>MARCO DELANE</h4>
    <div class="social"><span></span><span></span><span></span><span></span></div>
  </div>
  <div class="trainer" style="left:477px">
    <svg class="arch" viewBox="0 0 254 270"><path d="M14 230V127a113 113 0 0 1 226 0v45" fill="none" stroke="#fff" stroke-width="24"/></svg>
    <div class="portrait" role="img" aria-label="Portrait of trainer Evan Brooks"></div>
    <h4>EVAN BROOKS</h4>
    <div class="social"><span></span><span></span><span></span><span></span></div>
  </div>
  <div class="trainer" style="left:827px">
    <svg class="arch" viewBox="0 0 254 270"><path d="M14 230V127a113 113 0 0 1 226 0v45" fill="none" stroke="#fff" stroke-width="24"/></svg>
    <div class="portrait" role="img" aria-label="Portrait of trainer Tobias"></div>
    <h4>TOBIAS</h4>
    <div class="social"><span></span><span></span><span></span><span></span></div>
  </div>
  <div class="btn" style="left:510px;top:447px;width:196px;height:43px">View All Trainers <svg viewBox="0 0 10 14"><path d="M2 1l6 6-6 6" fill="none" stroke="#fff" stroke-width="2"/></svg></div>
</section>

<section class="contact">
  <div class="map" role="img" aria-label="Street map of the city around the club with a lake"></div>
  <h2 class="section-title">CONTACT US</h2>
  <div class="field" style="top:119px">Full name</div>
  <div class="field" style="top:172px">Phone #</div>
  <div class="field" style="top:223px">Email Address</div>
  <div class="field" style="top:271px;height:84px">Message</div>
  <div class="btn">SEDN NOW</div>
</section>

<footer class="site-footer">
  <div class="brand"><span class="dot"></span><span class="name">THE LANTERN</span></div>
  <p class="blurb">Lorem Ipsum is simply dummy text of the printing and typesetting industry.</p>
  <span class="more">READ MORE</span>
  <div class="social"><span></span><span></span><span></span><span></span></div>

  <h5 style="left:462px">QUICK LINK</h5>
  <ul class="quick" style="left:462px;top:184px">
    <li>Home</li><li>About</li><li>Services</li><li>Classes</li><li>Schedule</li><li>Trainers</li><li>Blog</li><li>Contact</li>
  </ul>

  <h5 style="left:652px">CONTACT US</h5>
  <ul class="reach" style="left:652px;top:184px;width:200px">
    <li><svg viewBox="0 0 12 12"><path d="M2 1h3l1 3-2 1a7 7 0 0 0 3 3l1-2 3 1v3c-6 0-9-3-9-9z" fill="#3ec3d0"/></svg>(+12) 555 014 2</li>
    <li><svg viewBox="0 0 12 12"><path d="M2 1h3l1 3-2 1a7 7 0 0 0 3 3l1-2 3 1v3c-6 0-9-3-9-9z" fill="#3ec3d0"/></svg>(+12) 555 014 3</li>
    <li><svg viewBox="0 0 12 12"><rect x="1" y="2" width="10" height="8" fill="#3ec3d0"/><path d="M1 2l5 4 5-4" fill="none" stroke="#000"/></svg>info@thelantern.com</li>
    <li><svg viewBox="0 0 12 12"><path d="M6 0a4 4 0 0 0-4 4c0 3 4 8 4 8s4-5 4-8a4 4 0 0 0-4-4z" fill="#3ec3d0"/><circle cx="6" cy="4" r="1.5" fill="#000"/></svg>18 Harbor Lane<br>Coral Vista,<br>FL 33101</li>
  </ul>

  <h5 style="left:875px">NEWSLETTER</h5>
  <p class="news">Lorem Ipsum is simply dummy text of the printing.</p>
  <div class="email">Email</div>
  <div class="btn subscribe">Subscribe</div>

  <div class="rule"></div>
  <div class="legal" style="left:122px">© Copyright 2016 The Lantern - All Right Reserved</div>
  <div class="legal" style="right:119px">Privacy Policy - Terms &amp; Conditions</div>
</footer>

</body>
</html>
```